Graffiti removal company needs cool flyer

Beacon Rinse & Spray is a pressure washing company based in Alberta, Canada - we offer general power washing and graffiti removal services for residential & commercial properties. . We would like an edgy/cool 2 sided flyer created to hand out to business / possible door hanger style with specific focus on graffiti removal but also touching on the power washing we can provide. The flyer should have the added pictures (use some before & afters) & wording attached. The picture from Harlow Dome should be used as its a prominent sports arena. There should be some graffiti fonts used to convey the titles/ steps/headings but the look should be clean.
Contact info to appear on flyer
Company logo
Ph 780-555-0143
derek@beaconrinse.ca
www.beaconrinseandspray.ca

```html
<!DOCTYPE html>
<html lang="en">
<head>
<meta charset="utf-8">
<title>Beacon Rinse &amp; Spray – Graffiti Removal Flyer</title>
<link rel="stylesheet" href="https://fonts.googleapis.com/css2?family=Montserrat:wght@400;600;700;800;900&family=Rubik:wght@500;700;800&family=Barlow:wght@400;500;600&display=swap">
<style>
:root{
  --stage:#5b5b5b;
  --navy:#0f3a73;
  --navy-deep:#0a2c5c;
  --royal:#1463b8;
  --sky:#1ea3e0;
  --orange:#f26a1b;
  --yellow:#f9c416;
  --green:#46b549;
  --green-dark:#2e9a3a;
  --white:#ffffff;
  --ink:#111111;
  --grey-band:#9aa0a6;
}
*{box-sizing:border-box;margin:0;padding:0}
html,body{width:1200px;height:1194px;overflow:hidden}
body{background:var(--stage);position:relative;font-family:"Montserrat",sans-serif}

.flyer{position:absolute;width:354px;height:866px;overflow:hidden;background:var(--white);box-shadow:0 6px 18px rgba(0,0,0,.35)}
.flyer--front{left:226px;top:140px}
.flyer--back{left:620px;top:188px}
.layer{position:absolute;left:0;top:0;width:354px;height:866px}
.abs{position:absolute}

/* front */
.brand{left:54px;top:26px;display:flex;align-items:center;gap:12px}
.brand__mark{width:34px;height:34px;background:var(--navy)}
.brand__name{font-family:"Montserrat",sans-serif;font-weight:800;font-size:18px;line-height:20px;color:var(--navy);letter-spacing:.5px}
.hero-photo{left:0;top:84px;width:354px;height:420px;background:linear-gradient(180deg,#e6e9ec 0%,#b8c0c8 45%,#7d8894 100%)}
.title{left:38px;color:var(--white);font-weight:800}
.title--small{top:448px;font-size:22px}
.title--big{top:470px;font-size:47px;letter-spacing:-.5px;font-weight:900}
.feature{left:30px;width:300px;color:var(--white)}
.feature__icon{position:absolute;left:0;top:0;width:26px;height:26px}
.feature__head{margin-left:42px;font-weight:700;font-size:12.5px}
.feature__body{margin-left:42px;margin-top:8px;font-size:6.6px;line-height:8.4px;text-align:justify}
.feature__body + .feature__body{margin-top:7px}
.contact{left:30px;color:var(--ink)}
.contact__phone{display:flex;align-items:center;gap:6px;font-family:"Montserrat",sans-serif;font-weight:800;font-size:22px;letter-spacing:-.3px}
.contact__mail{display:flex;align-items:center;gap:8px;margin-top:4px;font-size:12px;font-weight:500}

/* back */
.easy{left:40px;top:14px;font-family:"Rubik",sans-serif;font-weight:800;font-size:29px;color:var(--white);letter-spacing:-.3px}
.sprayer-photo{left:0;top:40px;width:354px;height:470px;background:linear-gradient(160deg,#eeeeee 0%,#c9c9c9 50%,#a4a4a4 100%)}
.step-text{font-family:"Barlow",sans-serif;color:var(--ink)}
.step-num{font-family:"Rubik",sans-serif;font-weight:800;color:var(--white);font-size:30px}
.ring{position:absolute;width:124px;height:124px;border-radius:50%;border:4px solid var(--yellow);overflow:hidden}
.ring__photo{width:100%;height:100%}
.ring__label{position:absolute;top:10px;left:0;width:100%;text-align:center;font-family:"Rubik",sans-serif;font-weight:700;font-size:17px;color:var(--yellow);text-shadow:-1px -1px 0 var(--ink),1px -1px 0 var(--ink),-1px 1px 0 var(--ink),1px 1px 0 var(--ink)}
.closing{left:26px;top:738px;width:300px;font-family:"Barlow",sans-serif;font-size:6.8px;line-height:8.6px;color:var(--white);text-align:center}
.closing p + p{margin-top:6px}
.closing em{font-style:normal;color:var(--yellow);font-weight:600}
</style>
</head>
<body>

<!-- FRONT SIDE -->
<section class="flyer flyer--front">
  <div class="abs hero-photo" role="img" aria-label="Photo of the Harlow Dome sports arena with the company's service truck and pressure washing rig parked in front"></div>

  <svg class="layer" viewBox="0 0 354 866" aria-hidden="true">
    <defs>
      <linearGradient id="frontBlue" x1="0" y1="0" x2="0" y2="1">
        <stop offset="0" stop-color="#1552a0"/>
        <stop offset="1" stop-color="#0a2c5c"/>
      </linearGradient>
    </defs>
    <rect x="0" y="0" width="354" height="84" fill="#ffffff"/>
    <path d="M0 470 C110 480 240 440 354 430 L354 866 L0 866 Z" fill="url(#frontBlue)"/>
    <path d="M0 792 C120 770 250 770 354 815 L354 866 L0 866 Z" fill="var(--grey-band)"/>
    <path d="M0 800 C120 780 250 782 354 826 L354 866 L0 866 Z" fill="#ffffff"/>
  </svg>

  <div class="abs brand">
    <span class="brand__mark"></span>
    <span class="brand__name">BEACON<br>RINSE &amp; SPRAY</span>
  </div>

  <div class="abs title title--small">GRAFFITI</div>
  <div class="abs title title--big">REMOVAL</div>

  <div class="abs feature" style="top:530px">
    <svg class="feature__icon" viewBox="0 0 26 26" fill="none" stroke="#fff" stroke-width="1.3"><circle cx="13" cy="7" r="4"/><path d="M11 7l1.5 1.5L15 5.5"/><path d="M3 18l5-4h5l3 2h3l4-2M4 21l5-3M22 21l-5-3"/></svg>
    <div class="feature__head">Trusted –</div>
    <p class="feature__body">Beacon Rinse &amp; Spray provides commercial graffiti removal services in the City of Edmonton &amp; Surrounding areas. We provide effective removal solutions for businesses affected by graffiti vandalism.</p>
  </div>

  <div class="abs feature" style="top:596px">
    <svg class="feature__icon" viewBox="0 0 26 26" fill="none" stroke="#fff" stroke-width="1.3"><circle cx="15" cy="15" r="8"/><path d="M15 10v5l3 2M13 4h4M2 12h5M3 16h4M4 20h4"/></svg>
    <div class="feature__head">Quick Response –</div>
    <p class="feature__body">We are here to help! Once we receive your call, Our team will arrange a site visit within 24 hrs to assess the surface, quote for the service, and then remove the graffiti. Beacon is committed to helping your business maintain a clean and professional property appearance. Your image matters to us!</p>
  </div>

  <div class="abs feature" style="top:676px">
    <svg class="feature__icon" viewBox="0 0 26 26" fill="none" stroke="#fff" stroke-width="1.3"><circle cx="7" cy="8" r="3"/><circle cx="13" cy="6" r="3"/><circle cx="19" cy="8" r="3"/><path d="M2 21v-6h10v6M14 21v-6h10v6"/></svg>
    <div class="feature__head">About us –</div>
    <p class="feature__body">We have been in business since 2011, providing power washing &amp; graffiti removal cleaning solutions. We are one of the largest Power washing companies within Edmonton!</p>
    <p class="feature__body">Why is it important to remove graffiti quickly? Graffiti tags are often viewed as 'calling cards' for the vandals that leave them. Simply put – one tag will encourage another, and another, and another to the same area. The best way to prevent graffiti is to quickly remove it. Removing it will also put you in compliance with Edmonton's Community Standards Bylaw 14600.</p>
  </div>

  <div class="abs contact" style="top:812px">
    <div class="contact__phone">
      <svg width="12" height="22" viewBox="0 0 12 22" fill="none" stroke="#111" stroke-width="2"><rect x="1" y="1" width="10" height="20" rx="2"/><path d="M4 17h4"/></svg>
      780-555-0143
    </div>
    <div class="contact__mail">
      <svg width="13" height="9" viewBox="0 0 13 9"><rect width="13" height="9" fill="#111"/><path d="M0 0l6.5 5L13 0" stroke="#fff" fill="none"/></svg>
      info@beaconrinseandspray.ca
    </div>
  </div>
</section>

<!-- BACK SIDE -->
<section class="flyer flyer--back">
  <div class="abs sprayer-photo" role="img" aria-label="Greyscale photo of a technician in safety gear pressure washing a brick wall"></div>

  <svg class="layer" viewBox="0 0 354 866" aria-hidden="true">
    <defs>
      <linearGradient id="backBlue" x1="0" y1="0" x2="0" y2="1">
        <stop offset="0" stop-color="#123f80"/>
        <stop offset="1" stop-color="#0a2c5c"/>
      </linearGradient>
    </defs>
    <path d="M0 0 H354 V52 C260 72 140 74 0 56 Z" fill="var(--royal)"/>
    <path d="M0 345 C110 350 250 390 354 450 L354 866 L0 866 Z" fill="url(#backBlue)"/>

    <!-- step 01 -->
    <rect x="70" y="96" width="250" height="46" fill="var(--yellow)"/>
    <rect x="40" y="86" width="60" height="66" fill="var(--orange)"/>
    <path d="M40 86 L52 78 H112 L100 86 Z" fill="#e35812"/>
    <text x="54" y="132" class="step-num">01</text>
    <text x="108" y="112" class="step-text" font-size="11" font-weight="500">Call for a free quote -</text>
    <text x="108" y="136" font-family="Rubik, sans-serif" font-weight="800" font-size="22" fill="#111">780-555-0143</text>

    <!-- step 02 -->
    <rect x="28" y="196" width="250" height="46" fill="var(--sky)"/>
    <rect x="262" y="186" width="64" height="68" fill="#1d6dc4"/>
    <path d="M262 254 L274 262 H338 L326 254 Z" fill="#1656a0"/>
    <text x="276" y="232" class="step-num">02</text>
    <text class="step-text" font-size="6.6" font-weight="600" fill="#111">
      <tspan x="34" y="206">Beacon Rinse &amp; Spray arrives within 24 hrs to</tspan>
      <tspan x="34" y="214">identify the tag (examine the substrate &amp; surface</tspan>
      <tspan x="34" y="222">), provide quote, schedule removal of graffiti with</tspan>
      <tspan x="34" y="230">eco-friendly biodegradable solutions &amp; pressure</tspan>
      <tspan x="34" y="238">wash the area clean.</tspan>
    </text>

    <!-- step 03 -->
    <rect x="70" y="290" width="250" height="46" fill="var(--green)"/>
    <rect x="40" y="280" width="62" height="66" fill="var(--green-dark)"/>
    <path d="M40 280 L52 272 H114 L102 280 Z" fill="#2a8a34"/>
    <text x="54" y="326" class="step-num">03</text>
    <text class="step-text" font-size="8.5" font-weight="500" fill="#111">
      <tspan x="118" y="306">Provide before and after photos</tspan>
      <tspan x="118" y="317">documenting the removal of the</tspan>
      <tspan x="118" y="328">graffiti.</tspan>
    </text>

    <path d="M0 792 C120 810 250 830 354 842 L354 866 L0 866 Z" fill="var(--grey-band)"/>
    <path d="M0 800 C120 818 250 838 354 852 L354 866 L0 866 Z" fill="#ffffff"/>
    <path d="M0 800 C120 818 250 838 354 852" fill="none"/>
  </svg>

  <div class="abs easy">Easy as 1 , 2 , 3</div>

  <div class="ring" style="left:22px;top:410px">
    <div class="ring__photo" role="img" aria-label="Before: concrete wall under glass railing with a spray-painted tag" style="background:linear-gradient(180deg,#8fa3b3 0%,#c9cdd1 55%,#b5b7b8 100%)"></div>
    <span class="ring__label">Before</span>
  </div>
  <div class="ring" style="left:178px;top:424px">
    <div class="ring__photo" role="img" aria-label="After: the same concrete wall cleaned with the tag removed" style="background:linear-gradient(180deg,#8fa3b3 0%,#d4d6d8 55%,#c2c3c4 100%)"></div>
    <span class="ring__label">After</span>
  </div>
  <div class="ring" style="left:14px;top:574px">
    <div class="ring__photo" role="img" aria-label="Before: brick building wall covered with graffiti tags" style="background:linear-gradient(160deg,#b8c4cf 0%,#9b6a4f 45%,#7d5a45 100%)"></div>
    <span class="ring__label">Before</span>
  </div>
  <div class="ring" style="left:166px;top:588px">
    <div class="ring__photo" role="img" aria-label="After: the same brick wall clean under a blue sky" style="background:linear-gradient(160deg,#3d7fd1 0%,#9a6f55 50%,#7a5a46 100%)"></div>
    <span class="ring__label">After</span>
  </div>

  <div class="abs closing">
    <p>Studies have shown the best strategy for the prevention of further graffiti is immediate removal. The longer graffiti lingers, the more graffiti and vandalism it attracts.</p>
    <p>No matter what's been put on your property it won't be there for long when you Call Beacon Rinse &amp; Spray. <em>Phone 780-555-0143</em></p>
  </div>

  <div class="abs contact" style="top:812px;left:40px">
    <div class="contact__phone">
      <svg width="12" height="22" viewBox="0 0 12 22" fill="none" stroke="#111" stroke-width="2"><rect x="1" y="1" width="10" height="20" rx="2"/><path d="M4 17h4"/></svg>
      780-555-0143
    </div>
    <div class="contact__mail">
      <svg width="13" height="9" viewBox="0 0 13 9"><rect width="13" height="9" fill="#111"/><path d="M0 0l6.5 5L13 0" stroke="#fff" fill="none"/></svg>
      info@beaconrinseandspray.ca
    </div>
  </div>
</section>

</body>
</html>
```